We need a new design for our construction website

We need a new website for our wordpress site kerrowmade.co.nz

It needs to be only a few pages but sleek in design and responsive, beautifully showcasing our images and video. Currently we have
1. home
2. about us
3. contact
We need either a front page that is designed much better to showcase more content, or potentially a projects page which has images from our builds. We don't have a lot of content so the content we do have needs to be maximised by image, rather than project.

Target Market(s)

High end residential construction and renovation projects, people wanting to build a nice home, clients based in Mount Maunganui, Tauranga.

Coding

Font styles to use
Sans Serif

Colors

Designer to choose only greyscale colors for use in the design.

Requirements
Must have
• A sleek design, architectural

```html
<!DOCTYPE html>
<html lang="en">
<head>
<meta charset="utf-8">
<title>Kerrowmade — Home</title>
<link href="https://fonts.googleapis.com/css2?family=Montserrat:wght@400;500;600&family=Roboto:ital,wght@0,400;0,500;1,400&display=swap" rel="stylesheet">
<style>
  :root{
    --ink:#2b2b2b;
    --text:#4a4a4a;
    --muted:#7a7a7a;
    --rule:#cfcfcf;
    --strip:#8c8c8c;
    --footer:#e6e6e6;
    --white:#ffffff;
    --hero-dark:#2a2826;
    --hero-mid:#4c4742;
  }
  *{margin:0;padding:0;box-sizing:border-box}
  html,body{width:1200px;height:3371px;overflow:hidden;background:var(--white)}
  body{position:relative;font-family:"Roboto",Arial,sans-serif;color:var(--text)}
  .abs{position:absolute}

  /* hero */
  .hero{left:0;top:0;width:1200px;height:590px;
    background:linear-gradient(100deg,#1f1d1b 0%,var(--hero-mid) 45%,#6b655d 70%,#3a3632 100%)}
  .brand{font-family:"Montserrat",sans-serif;font-weight:400;letter-spacing:10px;display:flex;align-items:center;gap:12px}
  .brand .dot{width:12px;height:12px;border:2px solid currentColor;border-radius:50%}
  .hero .brand{left:173px;top:30px;color:var(--white);font-size:27px}
  .nav-rule{left:517px;top:76px;width:683px;height:1px;background:rgba(255,255,255,.55)}
  .nav a{position:absolute;top:37px;font-family:"Montserrat",sans-serif;font-weight:600;font-size:13px;letter-spacing:1.2px;color:var(--white);text-decoration:none}
  .nav-active{left:522px;top:74px;width:43px;height:4px;background:var(--white)}
  .slide-dots span{position:absolute;left:37px;width:10px;height:10px;border-radius:50%;background:var(--white)}
  .slide-dots span.current{background:transparent;border:1.5px solid var(--white)}
  .social{left:28px;top:526px;font-family:"Montserrat",sans-serif;font-size:11px;letter-spacing:1px;color:var(--white)}

  /* section headings */
  .heading{left:174px;font-family:"Montserrat",sans-serif;font-weight:400;font-size:28px;letter-spacing:2.5px;color:var(--ink)}
  .heading-rule{left:0;width:280px;height:3px;background:var(--rule)}

  /* about */
  .about-col{top:732px;width:248px;font-size:12.2px;line-height:21px;text-align:justify;color:var(--text)}
  .about-mark{left:785px;top:707px;width:240px;height:274px;display:flex;align-items:center;justify-content:center;gap:10px;
    font-family:"Montserrat",sans-serif;font-size:20px;letter-spacing:5px;color:var(--muted)}
  .about-mark .dot{width:14px;height:14px;border-radius:50%;background:var(--rule)}

  /* projects */
  .strip{background:var(--strip)}
  .photo{background:linear-gradient(180deg,#7f96b6 0%,#a9b4bf 40%,#6e6660 100%)}
  .card-title{font-family:"Montserrat",sans-serif;font-size:19px;line-height:25px;color:var(--ink);width:330px}
  .view{font-family:"Montserrat",sans-serif;font-size:10.5px;font-weight:600;letter-spacing:1px;color:var(--muted);display:flex;align-items:center;gap:8px}

  /* services */
  .tile{top:2251px;width:297px;height:387px;display:flex;align-items:flex-end;justify-content:center;padding-bottom:38px}
  .tile span{font-family:"Montserrat",sans-serif;font-size:17px;letter-spacing:1.5px;line-height:20px;color:var(--white);text-align:center}

  /* testimonial */
  .quote-card{left:171px;top:2800px;width:578px;height:219px;background:var(--white);box-shadow:0 0 8px rgba(0,0,0,.14)}
  .quote-text{left:213px;top:2843px;width:460px;font-style:italic;font-size:12.4px;line-height:25px;color:var(--text)}
  .quote-mark{font-family:"Montserrat",sans-serif;font-size:58px;color:#c9c9c9;font-style:italic;line-height:1}
  .quote-name{left:219px;top:2971px;font-weight:500;font-size:13.5px;color:var(--ink)}

  /* footer */
  .footer{left:0;top:3084px;width:1200px;height:287px;background:var(--footer)}
  .footer .brand{left:174px;top:3160px;font-size:25px;color:var(--text)}
  .contact-line{left:173px;font-family:"Montserrat",sans-serif;font-size:15px;letter-spacing:.5px;color:var(--text)}
  .f-col h4{font-family:"Montserrat",sans-serif;font-weight:500;font-size:13.5px;letter-spacing:2px;color:var(--muted);margin-bottom:11px}
  .f-col li{list-style:none;font-size:11.5px;line-height:19.6px;color:var(--muted)}
  .footer-rule{left:160px;top:3320px;width:869px;height:1px;background:var(--rule)}
  .copyright{left:0;top:3339px;width:1200px;text-align:center;font-size:11.5px;color:var(--text)}
</style>
</head>
<body>

<!-- hero -->
<div class="abs hero" role="img" aria-label="Dimmed video still of a bright open-plan kitchen and dining room with children at a round table"></div>
<div class="abs brand"><span class="dot"></span>KERROWMADE</div>
<div class="abs nav-rule"></div>
<nav class="nav">
  <a style="left:525px">HOME</a>
  <a style="left:616px">ABOUT</a>
  <a style="left:709px">CONTACT</a>
  <a style="left:824px;display:flex;align-items:center;gap:7px">
    <svg width="13" height="13" viewBox="0 0 24 24"><path fill="#fff" d="M6.6 10.8a15.1 15.1 0 0 0 6.6 6.6l2.2-2.2a1 1 0 0 1 1-.25 11.4 11.4 0 0 0 3.6.57 1 1 0 0 1 1 1V20a1 1 0 0 1-1 1A17 17 0 0 1 3 4a1 1 0 0 1 1-1h3.5a1 1 0 0 1 1 1c0 1.25.2 2.45.57 3.6a1 1 0 0 1-.25 1z"/></svg>
    PH: 0275550142</a>
  <a style="left:1012px;top:35px">
    <svg width="16" height="16" viewBox="0 0 16 16"><circle cx="6.5" cy="6.5" r="4.8" fill="none" stroke="#fff" stroke-width="2"/><line x1="10" y1="10" x2="14.5" y2="14.5" stroke="#fff" stroke-width="2"/></svg>
  </a>
</nav>
<div class="abs nav-active"></div>
<div class="slide-dots">
  <span class="current" style="top:264px"></span>
  <span style="top:286px"></span>
  <span style="top:306px"></span>
  <span style="top:326px"></span>
</div>
<svg class="abs" style="left:564px;top:276px" width="70" height="70" viewBox="0 0 70 70">
  <circle cx="35" cy="35" r="33" fill="none" stroke="#fff" stroke-width="2.5"/>
  <path d="M28 23 L48 35 L28 47 Z" fill="#fff"/>
</svg>
<div class="abs social">FOLLOW</div>
<svg class="abs" style="left:572px;top:538px" width="54" height="18" viewBox="0 0 54 18">
  <polyline points="1,1 27,16 53,1" fill="none" stroke="rgba(255,255,255,.7)" stroke-width="1.2"/>
</svg>

<!-- about -->
<h2 class="abs heading" style="top:657px">ABOUT KERROWMADE</h2>
<div class="abs heading-rule" style="top:705px"></div>
<p class="abs about-col" style="left:173px">Ridgeline Homes Ltd T/A Kerrowmade was founded in 1985 by Graham Whitlock and began trading as Kerrowmade in 2017 with sons Liam and Owen at the helm. With the company's roots previously in solid timber, the team have a special interest in architectural homes, alternative building technologies and sustainable building practices. Kerrowmade's team have an exceptional understanding of alternative building materials and are happy to work with your architect or designer to ensure your build is as enjoyable and hassle-free as possible.</p>
<p class="abs about-col" style="left:480px">Liam has more than 15 years building experience and is our Managing Director, he is described by our customers as a problem solver, personable, down to earth and passionate about quality and the building performance of homes. Owen is Kerrowmade's Site Manager and has a passion for technical construction and alternative building technologies. Together Liam &amp; Owen provide clients with a strong foundation of knowledge, skill and care, providing attention to detail across the entire project and its management.</p>
<div class="abs about-mark"><span class="dot"></span>KERROWMADE</div>

<!-- projects -->
<h2 class="abs heading" style="top:1102px">OUR PROJECTS</h2>
<div class="abs heading-rule" style="top:1150px"></div>

<div class="abs strip" style="left:171px;top:1207px;width:42px;height:418px"></div>
<div class="abs photo" style="left:171px;top:1207px;width:406px;height:346px" role="img" aria-label="Timber floor framing under construction beside the sea with a tall pine tree"></div>
<div class="abs card-title" style="left:236px;top:1570px">Neque porro quisquaest qui dolor em ipsum quia dol sit ame</div>
<div class="abs view" style="left:236px;top:1633px">VIEW PROJECT <svg width="18" height="6" viewBox="0 0 18 6"><path d="M0 3h16M13 0.5l3 2.5-3 2.5" fill="none" stroke="#7a7a7a"/></svg></div>

<div class="abs strip" style="left:627px;top:1101px;width:52px;height:396px"></div>
<div class="abs photo" style="left:627px;top:1101px;width:400px;height:287px;background:linear-gradient(180deg,#9aa6b0 0%,#b07a4a 45%,#6a5a4c 100%)" role="img" aria-label="Covered outdoor room with timber louvre screens and a stone fireplace"></div>
<div class="abs card-title" style="left:701px;top:1406px">Neque porro quisquaest qui dolor em ipsum quia dol sit ame</div>
<div class="abs view" style="left:701px;top:1468px">VIEW PROJECT <svg width="18" height="6" viewBox="0 0 18 6"><path d="M0 3h16M13 0.5l3 2.5-3 2.5" fill="none" stroke="#7a7a7a"/></svg></div>

<div class="abs strip" style="left:627px;top:1555px;width:52px;height:388px"></div>
<div class="abs photo" style="left:627px;top:1555px;width:400px;height:268px;background:linear-gradient(180deg,#6f8fb8 0%,#b9bcbc 45%,#8a8278 100%)" role="img" aria-label="New gabled house with vertical cladding under a blue sky"></div>
<div class="abs card-title" style="left:701px;top:1841px">Neque porro quisquaest qui dolor em ipsum quia dol sit ame</div>
<div class="abs view" style="left:701px;top:1904px">VIEW PROJECT <svg width="18" height="6" viewBox="0 0 18 6"><path d="M0 3h16M13 0.5l3 2.5-3 2.5" fill="none" stroke="#7a7a7a"/></svg></div>

<div class="abs strip" style="left:171px;top:1705px;width:42px;height:312px"></div>
<div class="abs photo" style="left:171px;top:1705px;width:406px;height:237px;background:linear-gradient(180deg,#3f5a3a 0%,#5a6a48 40%,#a8683a 70%,#7a6a5a 100%)" role="img" aria-label="Cedar-clad cabin with a deck set against bush"></div>
<div class="abs card-title" style="left:236px;top:1960px">Neque porro quisquaest qui dolor em ipsum quia dol sit ame</div>
<div class="abs view" style="left:236px;top:2023px">VIEW PROJECT <svg width="18" height="6" viewBox="0 0 18 6"><path d="M0 3h16M13 0.5l3 2.5-3 2.5" fill="none" stroke="#7a7a7a"/></svg></div>

<!-- services -->
<h2 class="abs heading" style="top:2150px">WHAT WE DO</h2>
<div class="abs heading-rule" style="top:2199px"></div>
<div class="abs tile" style="left:0;background:linear-gradient(180deg,#2f5f9a 0%,#8a6a48 55%,#2e2a26 100%)" role="img" aria-label="Timber house frame on piles against a blue sky"><span>DESIGN &amp;<br>BUILD</span></div>
<div class="abs tile" style="left:301px;background:linear-gradient(180deg,#5a3a2a 0%,#8a4a2e 50%,#2a2422 100%)" role="img" aria-label="Renovated kitchen with pendant lights and a timber island"><span>RENOVATIONS<br>&amp; ADDITIONS</span></div>
<div class="abs tile" style="left:602px;background:linear-gradient(180deg,#6f94c8 0%,#a9b2bb 40%,#3a3836 100%)" role="img" aria-label="Dark-clad new home with a builder's site sign"><span>PROJECT<br>MANAGEMENT</span></div>
<div class="abs tile" style="left:903px;width:297px;background:linear-gradient(180deg,#3d4a3a 0%,#cfd8e2 45%,#3a4250 100%)" role="img" aria-label="Sunlit deck with outdoor furniture among trees"><span>BUILD SMARTER</span></div>

<!-- testimonials -->
<h2 class="abs heading" style="top:2721px">TESTIMONIALS</h2>
<div class="abs heading-rule" style="top:2768px"></div>
<div class="abs quote-card"></div>
<div class="abs quote-mark" style="left:205px;top:2826px">“</div>
<p class="abs quote-text">&nbsp;&nbsp;&nbsp;&nbsp;&nbsp;&nbsp;Our home is the envy of many friends. It holds the warmth incredibly through the winter and is perfectly cool in the summer. The ease of design has made it not only very smart with a modern feel but also with its strong robust construction it feels safe and secure for our young family. We love our home!</p>
<div class="abs quote-mark" style="left:557px;top:2920px">”</div>
<div class="abs quote-name">-Maren</div>
<div class="abs" style="left:766px;top:2761px;width:259px;height:219px;background:linear-gradient(180deg,#d9b48a 0%,#c49a70 50%,#4a4644 100%)" role="img" aria-label="Warm timber-lined living room with a grey sofa"></div>

<!-- footer -->
<footer>
  <div class="abs footer"></div>
  <div class="abs brand"><span class="dot"></span>KERROWMADE</div>
  <div class="abs contact-line" style="top:3231px">Ph:0275550142</div>
  <div class="abs contact-line" style="top:3261px">E:admin@kerrowmade.co.nz</div>
  <div class="abs f-col" style="left:496px;top:3149px">
    <h4>COMPANY</h4>
    <ul><li>Lorem ipsum dolo</li><li>Consecteing elit.</li><li>Fusce eget leo tincid</li><li>Donec consequat</li><li>Jmauris posueret</li></ul>
  </div>
  <div class="abs f-col" style="left:705px;top:3149px">
    <h4>INFORMATION</h4>
    <ul><li>Lorem ipsum dolo</li><li>Consecteing elit.</li><li>Fusce eget leo tincid</li><li>Donec consequat</li><li>Jmauris posueret</li></ul>
  </div>
  <div class="abs f-col" style="left:912px;top:3149px">
    <h4>OTHER LINKS</h4>
    <ul><li>Lorem ipsum dolo</li><li>Consecteing elit.</li><li>Fusce eget leo tincid</li><li>Donec consequat</li><li>Praesent elemen</li></ul>
  </div>
  <div class="abs footer-rule"></div>
  <div class="abs copyright">Copyright 2020 All Rights Reserved</div>
</footer>

</body>
</html>
```